Mara Lindqvist Advisory Business Cards

Hi - using the information and logo provided I require a two sided business card designed with the following information. The business card is a 'mini card' 3.5" x 1.25".

Front of card should be the logo attached but inverted (so the background is the peach colour and the logo white).

Back should have these details. If we can't fit the Instragram and Facebook part can we just put the little logos.

Mara Lindqvist

Art and Design Consultant
Dealer - Curator - Events - Styling - Creative Sourcing

P: 0438 519 207
E: mara@maralindqvistadvisory.com
W: www.maralindqvistadvisory.com
I (instagram image please): maralindqvistadvisory F (Facebook image please): MaraLindqvistAdvisor

Target Market(s)

Galleries, artists, art buyers, interior design clients, event managers, creative types

Industry/Entity Type

Business

```html
<!DOCTYPE html>
<html lang="en">
<head>
<meta charset="utf-8">
<title>Mara Lindqvist Advisory – Mini Business Cards</title>
<link href="https://fonts.googleapis.com/css2?family=Cormorant+Garamond:wght@500&family=Open+Sans:ital,wght@0,400;0,600;0,700;1,700&display=swap" rel="stylesheet">
<style>
  :root {
    --peach: #f3b99e;
    --peach-soft: #f7cdb8;
    --white: #ffffff;
    --cream: #fffec9;
    --page: #ffffff;
  }
  * { box-sizing: border-box; margin: 0; padding: 0; }
  html, body { width: 1200px; height: 991px; overflow: hidden; background: var(--page); }
  body { position: relative; font-family: "Open Sans", Arial, sans-serif; }

  .presentation {
    position: absolute; left: 0; top: 0; width: 1200px; height: 991px;
    background: var(--cream); border-radius: 40px;
  }

  .card {
    position: absolute; left: 83px; width: 1034px; height: 370px;
    border-radius: 120px 45px 120px 45px; overflow: hidden;
  }
  .card--front { top: 106px; background: var(--peach); }
  .card--back { top: 515px; background: var(--white); }

  .speech-bubble { position: absolute; left: 0; top: 0; width: 1034px; height: 370px; }

  .greeting-art {
    position: absolute; left: 515px; top: 90px; width: 350px; height: 205px;
    border-radius: 24px;
    background: linear-gradient(135deg, var(--peach-soft), var(--peach));
  }

  .brand {
    position: absolute; display: flex; align-items: center; gap: 10px;
    font-family: "Cormorant Garamond", Georgia, serif; font-weight: 500;
    letter-spacing: 0.08em; line-height: 1.05;
  }
  .brand__dot { width: 40px; height: 40px; border-radius: 50%; flex: none; }
  .brand__name span { display: block; }
  .brand__name .line-1 { font-size: 22px; }
  .brand__name .line-2 { font-size: 13px; letter-spacing: 0.18em; }

  .brand--front { left: 30px; top: 289px; color: var(--white); }
  .brand--front .brand__dot { background: var(--white); }

  .brand--back { left: 408px; top: 290px; color: var(--peach); }
  .brand--back .brand__dot { background: var(--peach); width: 36px; height: 36px; }
  .brand--back .brand__name .line-1 { font-size: 19px; }
  .brand--back .brand__name .line-2 { font-size: 11px; }

  .name-band {
    position: absolute; left: 0; top: 123px; width: 501px; height: 135px;
    background: var(--peach); color: var(--white); text-align: center;
  }
  .name-band__name {
    position: absolute; left: 0; right: 0; top: 29px;
    font-weight: 700; font-size: 30px; letter-spacing: 0.04em;
  }
  .name-band__rule {
    position: absolute; left: 0; right: 0; height: 1px; background: var(--white);
  }
  .name-band__rule--a { top: 70px; }
  .name-band__rule--b { top: 74px; }
  .name-band__role {
    position: absolute; left: 0; right: 0; top: 79px;
    font-size: 8.5px; font-weight: 600; line-height: 11px;
  }

  .contact-list {
    position: absolute; left: 527px; top: 123px; list-style: none;
  }
  .contact-list li {
    display: flex; align-items: center; gap: 9px; height: 27px;
    color: var(--peach); font-size: 10px; font-weight: 700; font-style: italic;
  }
  .contact-icon {
    width: 24px; height: 24px; background: var(--peach); border-radius: 2px;
    display: flex; align-items: center; justify-content: center; flex: none;
    color: var(--white); font-style: normal; font-size: 16px; font-weight: 600;
  }

  .name-panel {
    position: absolute; left: 757px; top: 123px; width: 277px; height: 135px;
    background: var(--peach); color: var(--white);
    display: flex; align-items: center; justify-content: center; text-align: center;
    font-family: "Cormorant Garamond", Georgia, serif; font-weight: 500;
    font-size: 24px; letter-spacing: 0.08em; line-height: 1.15;
  }
</style>
</head>
<body>
<div class="presentation">

  <section class="card card--front" aria-label="Card front">
    <svg class="speech-bubble" viewBox="0 0 1034 370" aria-hidden="true">
      <path fill="#ffffff" d="M347,338 C380,330 410,320 435,312 C440,340 445,360 452,370 L912,370 C960,310 985,240 988,150 C990,80 960,30 915,0 L605,0 C520,30 450,70 420,140 C400,190 412,250 395,280 C385,305 360,325 347,338 Z"/>
    </svg>
    <div class="greeting-art" role="img" aria-label="Hand-lettered greeting 'hello!!!' in peach script"></div>
    <div class="brand brand--front">
      <span class="brand__dot"></span>
      <span class="brand__name"><span class="line-1">MARA LINDQVIST</span><span class="line-2">ADVISORY</span></span>
    </div>
  </section>

  <section class="card card--back" aria-label="Card back">
    <div class="name-band">
      <h1 class="name-band__name">MARA LINDQVIST</h1>
      <span class="name-band__rule name-band__rule--a"></span>
      <span class="name-band__rule name-band__rule--b"></span>
      <p class="name-band__role">Art and Design Consultant<br>Dealer - Curator - Events - Styling - Creative Sourcing</p>
    </div>

    <ul class="contact-list">
      <li><span class="contact-icon">
        <svg width="14" height="16" viewBox="0 0 14 16" aria-hidden="true"><path fill="none" stroke="#fff" stroke-width="1.6" d="M4,1 L2,2 C0.5,5 2,11 7,14.5 L9,15 L10.5,12.5 L8,10.5 L6.5,11 C5,9.5 4,7 4,5 L5.5,4 Z"/></svg>
      </span>0438 519 207</li>
      <li><span class="contact-icon">
        <svg width="16" height="12" viewBox="0 0 16 12" aria-hidden="true"><rect x="1" y="1" width="14" height="10" fill="none" stroke="#fff" stroke-width="1.4"/><path d="M1,1 L8,7 L15,1" fill="none" stroke="#fff" stroke-width="1.4"/></svg>
      </span>mara@maralindqvistadvisory.com</li>
      <li><span class="contact-icon"></span>MaraLindqvistAdvisor</li>
      <li><span class="contact-icon"></span>maralindqvistadvisory</li>
      <li><span class="contact-icon">@</span>www.maralindqvistadvisory.com</li>
    </ul>

    <div class="name-panel">MARA LINDQVIST<br>ADVISORY</div>

    <div class="brand brand--back">
      <span class="brand__dot"></span>
      <span class="brand__name"><span class="line-1">MARA LINDQVIST</span><span class="line-2">ADVISORY</span></span>
    </div>
  </section>

</div>
</body>
</html>
```